front and back labels on a single sheet.

Vodka label design
Vodka is a colourless liquor. This vodka is tasteless and with no flavour.

FRONT LABEL
"FROST TALLY" is the brand name . it should be as big as possible.
below that " Only vodka made from sustainable means"
Remaining details to be copied from attached file.
Back Label
Details attached.

Colors
00AB8E
00BBA5
67D7C9
C6EFE9
E9F9F6

```html
<!DOCTYPE html>
<html lang="en">
<head>
<meta charset="utf-8">
<title>Frost Tally – Front and Back Labels</title>
<link rel="stylesheet" href="https://fonts.googleapis.com/css2?family=Antonio:wght@600&family=Cinzel:wght@400;600&family=Libre+Baskerville:wght@400;700&display=swap">
<style>
  :root{
    --gold:#c99a35;
    --gold-deep:#b8862a;
    --sheet:#eef0f0;
    --label:#ffffff;
    --on-gold:#ffffff;
  }
  *{box-sizing:border-box;margin:0;padding:0}
  html,body{width:1200px;height:1001px;overflow:hidden}
  body{background:var(--sheet);font-family:"Libre Baskerville",Georgia,serif;color:var(--gold)}
  .sheet{position:relative;width:1200px;height:1001px;display:flex;justify-content:center;align-items:center;gap:70px}
  .label{width:510px;height:600px;background:var(--label);display:flex;flex-direction:column;align-items:center;padding:44px 30px}

  /* front */
  .brand-mark{display:flex;align-items:center;gap:10px;margin-top:10px}
  .brand-mark__ring{width:46px;height:46px;border:2px solid var(--gold);border-radius:50%}
  .brand-mark__name{font-family:"Cinzel",serif;font-size:13px;letter-spacing:3px;font-weight:600}
  .front__kicker{font-family:"Cinzel",serif;font-size:22px;letter-spacing:6px;margin-top:26px}
  .rule{position:relative;width:100%;height:12px;display:flex;align-items:center;justify-content:center}
  .rule::before{content:"";position:absolute;left:0;right:0;top:50%;height:1px;background:var(--gold)}
  .rule__diamond{position:relative;width:11px;height:11px;background:var(--gold);transform:rotate(45deg)}
  .rule--plain .rule__diamond{display:none}
  .front__rule-top{margin-top:8px}
  .front__name{font-family:"Antonio",sans-serif;font-weight:600;font-size:112px;line-height:1;letter-spacing:-1px;margin:6px 0 4px;white-space:nowrap}
  .front__claim{font-family:"Libre Baskerville",serif;font-size:15px;font-weight:700;margin:14px 0 14px}
  .front__quality{font-family:"Cinzel",serif;font-size:15px;letter-spacing:5px;margin-top:30px}
  .front__facts{display:flex;align-items:center;justify-content:center;gap:26px;margin-top:30px}
  .front__fact{font-family:"Cinzel",serif;font-weight:600;font-size:17px;letter-spacing:4px}
  .spike{width:8px;height:120px}
  .maker-mark{display:flex;flex-direction:column;align-items:center;gap:8px;width:130px}
  .maker-mark__square{width:38px;height:38px;background:var(--gold)}
  .maker-mark__name{font-family:"Libre Baskerville",serif;font-weight:700;font-size:13px;letter-spacing:1px}

  /* back */
  .back{justify-content:center}
  .back__story{text-align:center;font-size:12px;line-height:1.75;letter-spacing:.3px}
  .back__story p+p{margin-top:10px}
  .back__rule{margin:10px 0}
  .notice-icons{display:flex;gap:26px;align-items:center;margin:6px 0}
  .notice-icon{width:46px;height:46px}
  .back__details{display:flex;width:100%;gap:28px;margin-top:12px;font-size:11px;line-height:1.5}
  .back__serve{width:42%}
  .back__serve .heading{margin-top:18px}
  .back__maker{flex:1}
  .heading{font-weight:700;font-size:11px}
  .back__maker .heading+p{margin-bottom:12px}
  .back__web{font-weight:700;font-size:15px;margin-top:6px}
  .back__band{width:100%;background:var(--gold);color:var(--on-gold);text-align:center;font-size:17px;letter-spacing:.5px;padding:10px 0;margin-top:20px}
</style>
</head>
<body>
<main class="sheet">

  <section class="label front" aria-label="Front label">
    <div class="brand-mark">
      <span class="brand-mark__ring"></span>
      <span class="brand-mark__name">FROST TALLY</span>
    </div>
    <p class="front__kicker">MADE FROM 5 SPICES</p>
    <div class="rule rule--plain front__rule-top"><span class="rule__diamond"></span></div>
    <h1 class="front__name">FROST TALLY</h1>
    <div class="rule"><span class="rule__diamond"></span></div>
    <p class="front__claim">ONLY VODKA MADE FROM SUSTAINABLE MEANS</p>
    <div class="rule"><span class="rule__diamond"></span></div>
    <p class="front__quality">PREMIUM QUALITY VODKA</p>
    <div class="front__facts">
      <span class="front__fact">50%</span>
      <svg class="spike" viewBox="0 0 8 120" aria-hidden="true"><polygon points="4,0 6,110 4,120 2,110" fill="var(--gold)"/></svg>
      <div class="maker-mark">
        <span class="maker-mark__square"></span>
        <span class="maker-mark__name">VERDANT STILL</span>
      </div>
      <svg class="spike" viewBox="0 0 8 120" aria-hidden="true"><polygon points="4,0 6,110 4,120 2,110" fill="var(--gold)"/></svg>
      <span class="front__fact">750ML</span>
    </div>
  </section>

  <section class="label back" aria-label="Back label">
    <div class="back__story">
      <p>THE ONLY VODKA IN THE WHOLE WORLD<br>WHICH HAS UNIQUE 5 SPICES, AND DISTILLED 3+1 TIMES</p>
      <p>IN ADDITION THIS IS THE ONLY VODKA MADE FROM NATURAL<br>RAINWATER &amp; SOLAR POWER, THUS MAKING IT THE ONLY<br>VODKA THAT IS SUSTAINABLY MANUFACTURED.</p>
    </div>
    <div class="rule back__rule"><span class="rule__diamond"></span></div>
    <div class="notice-icons">
      <svg class="notice-icon" viewBox="0 0 46 46" role="img" aria-label="Adults only symbol"><circle cx="23" cy="23" r="21" fill="var(--gold)"/></svg>
      <svg class="notice-icon" viewBox="0 0 46 46" role="img" aria-label="Not for pregnant women symbol"><circle cx="23" cy="23" r="20" fill="none" stroke="var(--gold)" stroke-width="3"/><line x1="9" y1="9" x2="37" y2="37" stroke="var(--gold)" stroke-width="3"/></svg>
      <svg class="notice-icon" viewBox="0 0 46 46" role="img" aria-label="Recyclable glass symbol"><polygon points="23,5 42,39 4,39" fill="none" stroke="var(--gold)" stroke-width="3"/></svg>
      <svg class="notice-icon" viewBox="0 0 46 46" role="img" aria-label="Standard drinks 27"><rect x="6" y="4" width="34" height="38" fill="none" stroke="var(--gold)" stroke-width="2"/><rect x="10" y="20" width="26" height="18" fill="var(--gold)"/><text x="23" y="34" text-anchor="middle" font-size="13" font-weight="700" fill="#fff" font-family="Libre Baskerville, serif">27</text></svg>
    </div>
    <div class="rule back__rule"><span class="rule__diamond"></span></div>
    <div class="back__details">
      <div class="back__serve">
        <p>This vodka has to be taken chilled with ice cubes. Making cocktails with lime and orange is a wonderful experience.</p>
        <p class="heading">CONTACT AT:</p>
        <p>contact@verdantstill.com.au</p>
      </div>
      <div class="back__maker">
        <p class="heading">FERMENTED AND DISTILLED BY:</p>
        <p>MARLOW J. EVERTON<br>AT VERDANT STILL PVT LTD</p>
        <p class="heading">MADE IN:</p>
        <p>BELLMERE, VICTORIA, AUSTRALIA</p>
        <p class="back__web">www.verdantstill.com.au</p>
      </div>
    </div>
    <p class="back__band">MADE FROM SUGARCANE</p>
  </section>

</main>
</body>
</html>
```